Business Card and Letterhead for Nurlo - modern real estate business

I need a double sided business card design for Nurlo. Please see business card brief here https://papers.trelvimo.net/sheet/q/7XrTbaLeZpMmQ2uWvd9HkCj4yNoEfsGi3lRtAz_pk/view?mode=shared

Please feel free to design the business cards however you feel best. I am happy to give some creative freedoms and then provide feedback from there.

Please then also create a letterhead to match the business card design

Colors

Designer to choose colors to be used in the design.

Requirements
Must have
• Must be a modern, elegant business card which looks very professional

```html
<!DOCTYPE html>
<html lang="en">
<head>
<meta charset="utf-8">
<title>Nurlo Stationery</title>
<link rel="stylesheet" href="https://fonts.googleapis.com/css2?family=Roboto:wght@400;500;700&display=swap">
<style>
  :root {
    --brand-red: #d8232a;
    --ink: #222222;
    --muted: #555555;
    --paper: #ffffff;
    --card-dark: #1c1c1c;
    --backdrop: #e9e9e9;
    --photo-a: #9aa38a;
    --photo-b: #3a3f3a;
  }
  * { box-sizing: border-box; margin: 0; padding: 0; }
  html, body { width: 1200px; height: 795px; overflow: hidden; }
  body {
    background: var(--backdrop);
    font-family: "Roboto", Arial, sans-serif;
    color: var(--ink);
    position: relative;
  }

  /* Letterhead */
  .letterhead {
    position: absolute; left: 70px; top: 40px;
    width: 505px; height: 714px;
    background: var(--paper);
    box-shadow: 0 6px 18px rgba(0,0,0,0.12);
  }
  .letterhead .wordmark {
    position: absolute; top: 52px; left: 0; right: 0;
    text-align: center;
    font-size: 52px; font-weight: 700; letter-spacing: 4px;
    color: var(--brand-red);
  }
  .rule { position: absolute; height: 1.5px; background: var(--brand-red); }
  .letterhead .rule-top { top: 130px; left: 40px; right: 40px; }
  .letterhead .rule-bottom { top: 606px; left: 40px; right: 40px; }
  .letterhead .contact-list {
    position: absolute; left: 44px; top: 622px;
    list-style: none; font-size: 12.5px; line-height: 21px;
  }
  .letterhead .address {
    position: absolute; right: 44px; top: 622px;
    text-align: right; font-size: 12.5px; line-height: 19px;
  }
  .contact-list li { display: flex; align-items: center; gap: 8px; }
  .icon { width: 12px; height: 12px; flex: none; color: var(--brand-red); }

  /* Card back */
  .card {
    position: absolute; width: 350px; height: 200px;
    box-shadow: 0 6px 16px rgba(0,0,0,0.14);
  }
  .card-back {
    left: 760px; top: 90px;
    background: var(--card-dark);
    display: flex; align-items: center; justify-content: center;
  }
  .card-back .wordmark {
    font-size: 56px; font-weight: 700; letter-spacing: 5px;
    color: var(--brand-red);
  }

  /* Card front */
  .card-front {
    left: 760px; top: 450px;
    background: var(--paper);
  }
  .card-front .portrait {
    position: absolute; left: 28px; top: 50px;
    width: 100px; height: 100px; border-radius: 50%;
    border: 3px solid var(--brand-red);
    background: radial-gradient(circle at 50% 40%, var(--photo-a), var(--photo-b));
  }
  .card-front .divider {
    position: absolute; left: 150px; top: 44px;
    width: 1.5px; height: 112px; background: var(--brand-red);
  }
  .card-front .details { position: absolute; left: 166px; top: 40px; }
  .card-front .name { font-size: 17px; font-weight: 700; }
  .card-front .name .first { color: var(--brand-red); }
  .card-front .role { font-size: 9.5px; color: var(--muted); margin-top: 2px; }
  .card-front .address { font-size: 9px; color: var(--muted); line-height: 13px; margin-top: 12px; }
  .card-front .contact-list { list-style: none; font-size: 9px; line-height: 15px; margin-top: 10px; }
  .card-front .contact-list li { gap: 6px; }
  .card-front .icon { width: 9px; height: 9px; }
</style>
</head>
<body>

<svg width="0" height="0" style="position:absolute" aria-hidden="true">
  <symbol id="icon-phone" viewBox="0 0 24 24"><path fill="currentColor" d="M6.6 10.8a15 15 0 0 0 6.6 6.6l2.2-2.2a1 1 0 0 1 1-.25 11.4 11.4 0 0 0 3.6.57 1 1 0 0 1 1 1V20a1 1 0 0 1-1 1A17 17 0 0 1 3 4a1 1 0 0 1 1-1h3.5a1 1 0 0 1 1 1c0 1.25.2 2.45.57 3.57a1 1 0 0 1-.25 1z"/></symbol>
  <symbol id="icon-mail" viewBox="0 0 24 24"><rect x="2.5" y="5" width="19" height="14" rx="1.5" fill="none" stroke="currentColor" stroke-width="2.2"/><path d="M3 6l9 7 9-7" fill="none" stroke="currentColor" stroke-width="2.2"/></symbol>
  <symbol id="icon-globe" viewBox="0 0 24 24"><circle cx="12" cy="12" r="9.5" fill="none" stroke="currentColor" stroke-width="2"/><ellipse cx="12" cy="12" rx="4" ry="9.5" fill="none" stroke="currentColor" stroke-width="2"/><path d="M2.5 12h19" stroke="currentColor" stroke-width="2"/></symbol>
</svg>

<section class="letterhead">
  <div class="wordmark">NURLO</div>
  <div class="rule rule-top"></div>
  <div class="rule rule-bottom"></div>
  <ul class="contact-list">
    <li><svg class="icon"><use href="#icon-phone"/></svg>Phone: 0412 555 308</li>
    <li><svg class="icon"><use href="#icon-mail"/></svg>E-mail: dane@nurlo.com</li>
    <li><svg class="icon"><use href="#icon-globe"/></svg>Website: www.nurlo.com</li>
  </ul>
  <div class="address">PO Box 3186<br>Linden Vale NSW 2790</div>
</section>

<section class="card card-back">
  <div class="wordmark">NURLO</div>
</section>

<section class="card card-front">
  <div class="portrait" role="img" aria-label="Portrait photo of the agent"></div>
  <div class="divider"></div>
  <div class="details">
    <div class="name"><span class="first">Dane</span> Morrow</div>
    <div class="role">Licensed Property Agent</div>
    <div class="address">PO Box 3186<br>Linden Vale NSW 2790</div>
    <ul class="contact-list">
      <li><svg class="icon"><use href="#icon-phone"/></svg>Phone: 0412 555 308</li>
      <li><svg class="icon"><use href="#icon-mail"/></svg>E-mail: dane@nurlo.com</li>
      <li><svg class="icon"><use href="#icon-globe"/></svg>Website: www.nurlo.com</li>
    </ul>
  </div>
</section>

</body>
</html>
```